Business is backhoe and truck hire. As the title indicates, we dig dirt. Colours preferred are charcoal, red and or orange. Would like a backhoe on the card,possibly a designs with the silhouette of the machine in the background. I We would like to incorporate a large tick in the title for solutions. I thought it could be part of the "W" . Our shirts are Black polo's with orange lines around sleeves and sides. We are a new business in rural Qld, happy to do the smaller jobs that others wont.

Industry/Entity Type

Business

Contact Information for Business Card

Tall Creek Groundworks Solutions

Backhoe and Truck Hire
ABN:58214096371

Peter Kellow
PH: 0491 736 204
PH: 0491 862 035
PH: 4283 6147 a/h

email: tcgsolutions@mailbox-example.com

```html
<!DOCTYPE html>
<html lang="en">
<head>
<meta charset="utf-8">
<title>Tall Creek Groundworks Solutions – Business Cards</title>
<link rel="stylesheet" href="https://fonts.googleapis.com/css2?family=Open+Sans:wght@400;600&family=Michroma&display=swap">
<style>
  :root {
    --backdrop: #cfcdcd;
    --charcoal: #2f3234;
    --charcoal-deep: #222527;
    --orange: #ef6a1f;
    --brand-red: #d8352a;
    --white: #ffffff;
    --silhouette-grey: #55595c;
    --text-light: #f2f2f2;
  }
  * { box-sizing: border-box; margin: 0; padding: 0; }
  html, body {
    width: 1200px; height: 900px; overflow: hidden;
    background: var(--backdrop);
    font-family: "Open Sans", sans-serif;
  }
  .canvas {
    position: relative; width: 1200px; height: 900px;
  }
  .card {
    position: absolute; top: 291px;
    width: 520px; height: 318px;
    border-radius: 24px; overflow: hidden;
    box-shadow: 0 10px 24px rgba(0,0,0,0.25);
  }
  .card--front {
    left: 50px;
    background: radial-gradient(ellipse at 50% 40%, var(--charcoal) 0%, var(--charcoal-deep) 100%);
  }
  .card--back {
    left: 630px;
    background: var(--charcoal-deep);
  }

  /* Front */
  .slogan {
    position: absolute; top: 34px; left: 0; right: 0;
    text-align: center;
    color: var(--orange);
    font-size: 21px; letter-spacing: 4px;
  }
  .brand-lockup {
    position: absolute; display: flex; align-items: center; gap: 8px;
  }
  .brand-mark {
    width: 14px; height: 14px; background: var(--brand-red); flex: none;
  }
  .brand-name {
    font-weight: 600; color: var(--brand-red); white-space: nowrap;
  }
  .card--front .brand-lockup { top: 120px; left: 40px; }
  .card--front .brand-name { font-size: 22px; }
  .service-line {
    position: absolute; font-family: "Michroma", sans-serif; white-space: nowrap;
  }
  .card--front .service-line {
    top: 158px; right: 52px; color: var(--text-light); font-size: 15px;
  }
  .machine-row {
    position: absolute; left: 24px; right: 24px; bottom: 28px; height: 70px;
    display: flex; align-items: flex-end; gap: 14px;
  }
  .machine-art {
    background: linear-gradient(180deg, #5d6164, var(--silhouette-grey));
    border-radius: 6px; opacity: 0.8;
  }
  .machine-art--xs { width: 64px; height: 30px; }
  .machine-art--s { width: 84px; height: 40px; }
  .machine-art--m { width: 104px; height: 52px; }
  .machine-art--l { width: 150px; height: 68px; }

  /* Back */
  .back-top {
    position: absolute; top: 0; left: 0; right: 0; height: 156px;
    background: var(--white);
  }
  .orange-stripe {
    position: absolute; top: 156px; left: 0; right: 0; height: 10px;
    background: var(--orange);
  }
  .card--back .brand-lockup { top: 52px; left: 38px; }
  .card--back .brand-name { font-size: 20px; }
  .card--back .service-line {
    top: 86px; left: 150px; color: var(--charcoal-deep); font-size: 13px;
  }
  .hero-machine {
    position: absolute; right: 20px; top: 70px; width: 92px; height: 82px;
    background: linear-gradient(180deg, #f38a4c, var(--orange));
    border-radius: 6px;
  }
  .contact-name {
    position: absolute; top: 178px; left: 30px;
    color: var(--orange); font-size: 16px;
  }
  .contact-list {
    position: absolute; top: 200px; left: 104px; list-style: none;
    color: var(--text-light);
  }
  .contact-list li {
    display: flex; align-items: center; gap: 6px;
    font-size: 16px; line-height: 22px;
  }
  .contact-list .email { font-size: 13.5px; }
  .contact-list svg { flex: none; }
  .abn {
    position: absolute; top: 292px; left: 126px;
    color: var(--text-light); font-size: 12px; font-weight: 600;
  }
</style>
</head>
<body>
<main class="canvas">

  <section class="card card--front" aria-label="Business card front">
    <p class="slogan">Big or Small, we do them all</p>
    <div class="brand-lockup">
      <span class="brand-mark"></span>
      <span class="brand-name">Tall Creek Groundworks Solutions</span>
    </div>
    <p class="service-line">Backhoe and Truck Hire</p>
    <div class="machine-row">
      <div class="machine-art machine-art--xs" role="img" aria-label="Faint grey backhoe silhouette, small"></div>
      <div class="machine-art machine-art--s" role="img" aria-label="Faint grey backhoe silhouette"></div>
      <div class="machine-art machine-art--m" role="img" aria-label="Faint grey backhoe silhouette, larger"></div>
      <div class="machine-art machine-art--l" role="img" aria-label="Faint grey backhoe silhouette, largest"></div>
    </div>
  </section>

  <section class="card card--back" aria-label="Business card back">
    <div class="back-top"></div>
    <div class="orange-stripe"></div>
    <div class="brand-lockup">
      <span class="brand-mark"></span>
      <span class="brand-name">Tall Creek Groundworks Solutions</span>
    </div>
    <p class="service-line">Backhoe and Truck Hire</p>
    <div class="hero-machine" role="img" aria-label="Orange backhoe silhouette"></div>

    <p class="contact-name">Peter Kellow</p>
    <ul class="contact-list">
      <li>
        <svg width="18" height="16" viewBox="0 0 18 16" aria-hidden="true"><path d="M2 6 Q9 0 16 6 L14 8 L12 6 L6 6 L4 8 Z M4 9 H14 V15 H4 Z" fill="var(--orange)"/><circle cx="9" cy="12" r="2" fill="var(--charcoal-deep)"/></svg>
        0491 736 204
      </li>
      <li>
        <svg width="18" height="16" viewBox="0 0 18 16" aria-hidden="true"><path d="M2 6 Q9 0 16 6 L14 8 L12 6 L6 6 L4 8 Z M4 9 H14 V15 H4 Z" fill="var(--orange)"/><circle cx="9" cy="12" r="2" fill="var(--charcoal-deep)"/></svg>
        0491 862 035
      </li>
      <li>
        <svg width="18" height="16" viewBox="0 0 18 16" aria-hidden="true"><path d="M2 6 Q9 0 16 6 L14 8 L12 6 L6 6 L4 8 Z M4 9 H14 V15 H4 Z" fill="var(--orange)"/><circle cx="9" cy="12" r="2" fill="var(--charcoal-deep)"/></svg>
        4283 6147
      </li>
      <li class="email">
        <svg width="18" height="14" viewBox="0 0 18 14" aria-hidden="true"><rect x="1" y="1" width="16" height="12" fill="none" stroke="var(--orange)" stroke-width="1.6"/><path d="M1 1 L9 8 L17 1" fill="none" stroke="var(--orange)" stroke-width="1.6"/></svg>
        tcgsolutions@mailbox-example.com
      </li>
    </ul>
    <p class="abn">ABN:58214096371</p>
  </section>

</main>
</body>
</html>
```